Brightwater Business Advisors - new Website

We already have completed the logo, the files attached are attached on this brief. Using the attached logo, please submit your designs for the Website.

2 updates for the sites to help clarify the requirements:

a) “Our Services will require a separate landing page each and some will require the ability to book an appointment on-line.”
- the end goal is to have the appointments link to my calendar.

b) "Services x 5 – Brightwater Office / Recruitment / Business Consulting Services / Virtual CFO / Online Skills Tests
- ability to book an initial consultation via an app such as Meetloop which links to my calendar

- no payments will take place online, but we will capture the visitors details via a form... similar to the newsletter sign-up

- the skill test will have a link that will direct the user to an external testing site
- no payments will take place on the site

Website (see detail below)
Menu Options: Home page / Our Team / Services / Training / Contact Us

Home page lay-out
1 - High Quality Main Picture
2. Products & Services (clickable) - Recruitment / Virtual Office / Business Advisors / Virtual CFO / Online Skills Tests
3. Picture - Training / Workshops (clickable)
4. Other links to pages - e-books / Whitepapers / Blogs / FAQs
- ability for me to create new blogs... similar to the Brightwaterpa website

Does not have to include everything on the home page... just links through-out the website for more information.

Looking for a clean website with summary information. Contact Us for more information or to make an appointment.

We have our own website hosting plan, so it will need to be moved across.

Search Engine Optimisation (SEO) is important to us - so you will need some knowledge on this - but we will provide you with material.

When the website is finalised, we will need access to make minor text changes internally. This is not a regular occurence. We rarely make changes.

Our Services will require a separate landing page each and some will require the ability to book an appointment on-line or to capture their details. Ability to add live chat feature later.

Definitely need logos at the bottom for Netlinker, Chirpster, Pinboardly, Friendpage, Searchly Circle and others.

Our website will need a corporate look and feel and we prefer to utilise various shades of blue through-out the site. It does not need to be a replica of our other 3 sites, but it should show that it is part of the group.

At the bottom of the page we should show links to our other 3 companies with the heading... Part of the following x3 affiliated companies:
Brightwater Innovation - Brightwater Growth Horizon - Brightwater Work Set
Logos will be provided if required.

Our business cards have also been uploaded for reference, but this is not necessarily the final - if you come up with a different design.

6. Content will be available early next week, so if you would like this information to personalise your design, let me know.

Special Note:
There is the possibility for further work - for a facelift change for one of our older sites. It currently is old and just needs a re-fresh to a simple design. It currently uses PHP, ASP and microsoft SQL. This could be the same lay-out as the Brightwater Business Advisors site - just different pictures and text.

Target Market(s)

small to medium sized businesses $1M - $10M turnover

Industry/Entity Type

Business Consultant

Contact Information for Business Card

When we get up to this, I can show you samples of our existing business cards, but I do not want this to overshadow the new design. I would like a list of our services on the back of the card and our contact details on the front.

Logo Text

Brightwater Business Advisors

Coding

Number of Pages Required

Colors
0456a4
3277b5
0592cd

Requirements
Must have
• approved Logo design - available in the uploads section
• Dark Blue, Corporate colours - similar to www.Brightwaterpa.example.com.au
• Over 20 years experience
Nice to have
• We are not in one industry, but some examples of clients we have worked with are in:
• Freight Industry
• Torvane FlameGuard Equipment, Halbrook Records, Kestra Motors Australia
• Contruction Industry - Plumbers, Builders, Contractors
• Real Estate Agents
• Retail - Beauticians, Physio, Hairdressers
Should not have
• Not too bright.
• As an example, see TallyrunCFO.example.com.au
• This is our old company, the website colours do not fit with the Brightwaterpa.example.com.au colours and are too vibrant... too colourful. It should be more blue and corporate. Most of all, it should look like it is part of the Group. It can have colour, but should not be overwhelmingly different.

```html
<!DOCTYPE html>
<html lang="en">
<head>
<meta charset="utf-8">
<title>Brightwater Business Advisors</title>
<link href="https://fonts.googleapis.com/css2?family=Montserrat:wght@400;500;600&family=Open+Sans:wght@400;600&display=swap" rel="stylesheet">
<style>
:root{
  --navy:#0456a4;
  --mid:#3277b5;
  --sky:#0592cd;
  --royal:#0a5cb0;
  --ink:#2d2d2d;
  --text:#777;
  --line:#dedede;
  --soft:#f3f3f3;
  --dark:#2a2a2a;
}
*{margin:0;padding:0;box-sizing:border-box}
html,body{width:1200px;height:5006px;overflow:hidden;background:#fff}
body{font-family:"Open Sans",Arial,sans-serif;color:var(--text);font-size:11px;position:relative}
h1,h2,h3,h4,.brand,.btn{font-family:"Montserrat",Arial,sans-serif}
section,header,nav,footer{position:absolute;left:0;width:1200px}
.abs{position:absolute}
a{color:inherit;text-decoration:none}
.link{color:var(--navy);text-decoration:underline;font-size:10px}
.section-title{position:absolute;left:0;width:1200px;text-align:center;font-weight:400;font-size:29px;color:var(--ink)}
.brand{font-weight:500;color:var(--navy);display:flex;align-items:center;gap:10px;white-space:nowrap}
.brand .mark{width:22px;height:22px;border-radius:50%;background:var(--navy);flex:none}
.ph{display:block}

/* header */
.site-header{top:0;height:122px}
.site-header .brand{left:130px;top:48px;font-size:21px}
.phone{left:467px;top:42px;display:flex;align-items:center;gap:14px}
.phone .ico{width:38px;height:38px;border-radius:50%;border:1px solid var(--line);display:flex;align-items:center;justify-content:center}
.phone small{display:block;font-size:10px;color:#555}
.phone b{font-weight:400;font-size:13px;color:#333}
.btn{position:absolute;border:2px solid var(--sky);border-radius:20px;color:var(--navy);font-weight:500;font-size:13px;display:flex;align-items:center;justify-content:center;gap:6px;background:#fff}
.main-nav{top:122px;height:53px;background:var(--soft);border-top:1px solid #e6e6e6}
.main-nav ul{list-style:none;position:absolute;left:130px;width:940px;height:53px;display:flex}
.main-nav li{flex:1;display:flex;align-items:center;justify-content:center;font-family:"Montserrat",sans-serif;font-size:11px;color:#333;border-right:1px solid #ddd}
.main-nav li:last-child{border-right:0}
.main-nav li.active{background:#fff;border-top:3px solid var(--navy);font-weight:600;flex:.75}

/* hero */
.hero{top:175px;height:580px;overflow:hidden}
.hero .photo{position:absolute;inset:0;background:linear-gradient(100deg,#a7b4c2 0%,#d9dfe6 30%,#eef0f2 50%,#8c9aa8 100%)}
.hero h1{left:130px;top:236px;font-size:47px;font-weight:500;color:#1c1c1c}
.hero .lead{left:150px;top:300px;width:360px;text-align:center;font-size:16px;color:#222;line-height:25px}
.dots{left:296px;top:368px;display:flex;gap:14px}
.dots i{width:12px;height:12px;border-radius:50%;border:2px solid #fff;display:block}
.dots i.on{background:var(--sky);border-color:var(--sky)}
.quote{left:770px;top:96px;width:298px;height:372px;background:rgba(40,40,40,.85);text-align:center;padding-top:28px;color:#fff}
.quote h2{font-weight:500;font-size:25px}
.quote p{font-size:10px;line-height:17px;margin:10px auto 18px;width:220px;color:#ddd}
.quote .field{width:252px;height:34px;margin:0 auto 6px;background:#fff;text-align:left;font-size:9px;color:#999;padding:10px 14px}
.quote .field.msg{height:74px}
.quote .send{position:static;margin:10px auto 0;width:142px;height:34px;background:var(--sky);color:#fff;border:0;font-size:14px}
.hero svg.curve{position:absolute;left:0;bottom:0}

/* story */
.story{top:755px;height:490px}
.story .pc{left:130px;top:70px;width:325px;height:335px;background:linear-gradient(#3a3a3a,#dcdcdc);border-radius:6px}
.story h2{left:557px;top:110px;font-size:28px;font-weight:400;color:var(--ink)}
.story .copy{left:557px;top:160px;width:510px;line-height:22px;font-size:11px}
.story .copy p{margin-bottom:20px}
.story .btn{left:557px;top:328px;width:105px;height:36px;font-size:11px}

/* team */
.team{top:1245px;height:540px;background:linear-gradient(135deg,#4f9ee0,#3180cc 60%,#4591d6)}
.team h2{color:#fff;top:68px}
.member{position:absolute;top:205px;width:216px;height:250px;background:#fff;text-align:center;padding-top:103px;box-shadow:6px 6px 0 rgba(0,0,0,.08)}
.member .avatar{position:absolute;left:41px;top:-65px;width:134px;height:134px;border-radius:50%;border:4px solid #fff;background:linear-gradient(#7d7d7d,#c5c5c5)}
.member h3{color:var(--navy);font-size:14px;font-weight:500}
.member .role{font-size:9px;color:#333;margin:6px 0 10px}
.member p{font-size:10px;line-height:19px;width:170px;margin:0 auto 10px}

/* services */
.services{top:1785px;height:407px}
.services .section-title{top:68px}
.svc{position:absolute;top:135px;width:290px;height:110px}
.svc .ring{position:absolute;left:0;top:0;width:92px;height:92px;border-radius:50%;border:1px solid var(--line);display:flex;align-items:center;justify-content:center}
.svc h4{position:absolute;left:108px;top:8px;font-weight:500;font-size:13px;color:#333;line-height:20px}
.svc p{position:absolute;left:108px;top:56px;width:180px;font-size:10px;line-height:20px}
.svc .more{position:absolute;left:108px;color:var(--navy);font-size:9px}
.services .btn{left:531px;top:300px;width:138px;height:38px;font-size:11px}

/* blogs */
.blogs{top:2192px;height:581px;background:var(--soft)}
.blogs .section-title{top:90px}
.post{position:absolute;top:166px;width:287px}
.post .frame{height:178px;background:#fff;padding:8px;border:1px solid #e2e2e2}
.post .frame span{width:100%;height:100%;background:linear-gradient(135deg,#c9b9a6,#6d7f93)}
.post h3{font-size:15px;font-weight:400;color:#333;margin:26px 0 10px}
.post .meta{font-size:10px;color:var(--navy);margin-bottom:14px}
.post p{font-size:10px;line-height:21px;margin-bottom:14px}

/* faqs */
.faqs{top:2773px;height:439px}
.faqs h2{left:130px;top:84px;font-size:29px;font-weight:400;color:var(--ink)}
.faq{position:absolute;left:130px;width:470px;border:1px solid var(--line);padding:10px 14px 10px 36px;font-size:12px;color:#333}
.faq:before{content:"?";position:absolute;left:12px;top:11px;width:13px;height:13px;border-radius:50%;border:1px solid var(--sky);color:var(--sky);font-size:9px;text-align:center;line-height:11px}
.faq:after{content:"+";position:absolute;right:12px;top:9px;width:11px;height:11px;border:1px solid #aaa;font-size:9px;line-height:9px;text-align:center;color:#888}
.faq p{font-size:10px;color:var(--text);line-height:21px;margin:6px 0}
.ebook{left:648px;top:93px;width:420px;height:254px;border:1px solid var(--line)}
.ebook .laptop{left:30px;top:44px;width:176px;height:176px;background:linear-gradient(#9d4c52,#3b3b3b 60%,#c9c9c9)}
.ebook h3{left:252px;top:58px;font-size:28px;font-weight:400;color:var(--ink)}
.ebook p{left:252px;top:104px;width:120px;font-size:10px;line-height:22px}
.ebook .go{left:372px;top:192px}

/* workshops */
.workshops{top:3212px;height:765px;background:var(--royal)}
.workshops .section-title{top:86px;color:#fff}
.tile{position:absolute;width:450px;height:248px;border:6px solid #fff;background:linear-gradient(135deg,#dfe4ea,#8f9eae)}
.tile span{position:absolute;left:0;bottom:38px;background:rgba(30,30,30,.85);color:#fff;font-family:"Montserrat",sans-serif;font-size:15px;padding:12px 24px 12px 20px}

/* products */
.products{top:3977px;height:360px}
.products .section-title{top:88px}

/* affiliates */
.affiliates{top:4337px;height:177px;border-top:1px solid #eee}
.affiliates .row{position:absolute;left:130px;top:72px;width:940px;display:flex;justify-content:space-between;align-items:center}
.affiliates .brand{font-size:18px}

/* mailing */
.mailing{top:4514px;height:159px;background:linear-gradient(90deg,#3a3a3a,#222);border-bottom:4px solid var(--navy)}
.mailing h3{left:245px;top:56px;color:#fff;font-weight:400;font-size:22px}
.mailing p{left:248px;top:90px;color:#ddd;font-size:12px}
.mailing .email{left:605px;top:62px;width:346px;height:40px;background:#fff;border-radius:20px 0 0 20px;font-size:10px;color:#888;padding:13px 20px}
.mailing .sub{left:950px;top:62px;width:118px;height:40px;background:var(--sky);color:#fff;font-family:"Montserrat",sans-serif;font-size:11px;font-weight:600;border-radius:0 20px 20px 0;text-align:center;line-height:40px}

/* footer */
.site-footer{top:4673px;height:333px;background:var(--soft)}
.site-footer .brand{left:130px;top:106px;font-size:17px}
.social{left:168px;top:180px;display:flex;gap:10px}
.social i{width:28px;height:28px;border-radius:50%;border:1px solid #555;display:block}
.col h4{font-size:13px;font-weight:500;color:#333;margin-bottom:26px}
.col li{list-style:none;font-size:10px;line-height:24px;color:#555}
.col p{font-size:10px;line-height:20px;color:#555;width:250px}
.col .box{width:250px;height:38px;background:#fff;border:1px solid #ddd;margin:16px 0 10px;font-size:9px;color:#999;padding:13px 12px}
.col .go{width:90px;height:28px;background:var(--navy);color:#fff;border-radius:14px;font-family:"Montserrat",sans-serif;font-size:9px;font-weight:600;text-align:center;line-height:28px}
.contact li{display:flex;gap:12px;align-items:flex-start;line-height:18px;margin-bottom:10px}
.contact li i{width:10px;height:10px;background:#555;border-radius:2px;margin-top:4px;flex:none}
.copyright{left:0;width:1200px;top:314px;text-align:center;font-size:10px;color:#555}
</style>
</head>
<body>

<header class="site-header">
  <div class="brand abs"><span class="mark"></span>Brightwater Innovation</div>
  <div class="phone abs">
    <span class="ico"><svg width="14" height="14" viewBox="0 0 24 24"><path fill="#333" d="M6.6 10.8a15 15 0 006.6 6.6l2.2-2.2a1 1 0 011-.25 11 11 0 003.5.56 1 1 0 011 1V20a1 1 0 01-1 1A17 17 0 013 4a1 1 0 011-1h3.5a1 1 0 011 1 11 11 0 00.56 3.5 1 1 0 01-.25 1z"/></svg></span>
    <div><small>Phone :</small><b>+61 (0)2 9000-1234</b></div>
  </div>
  <a class="btn" style="left:672px;top:42px;width:172px;height:42px"><svg width="13" height="13" viewBox="0 0 24 24"><circle cx="12" cy="12" r="10" fill="none" stroke="#0456a4" stroke-width="2"/><circle cx="12" cy="10" r="3.5" fill="#0456a4"/><path d="M6 18c2-3 10-3 12 0" stroke="#0456a4" stroke-width="2" fill="none"/></svg>Members Login</a>
  <a class="btn" style="left:850px;top:42px;width:218px;height:42px"><svg width="12" height="12" viewBox="0 0 24 24"><path d="M3 21l3-1 13-13-2-2L4 18z" fill="#0456a4"/></svg>Make an appointment</a>
</header>

<nav class="main-nav">
  <ul>
    <li class="active">HOME</li><li>OUR TEAM</li><li>SERVICES</li><li>PRODUCTS</li><li>WORKSHOPS TRAINING</li><li>FAQS</li><li>CONTACT US</li>
  </ul>
</nav>

<section class="hero">
  <div class="photo" role="img" aria-label="Photo of a smiling business advisor reviewing documents in an office"></div>
  <h1 class="abs">Business Advisor</h1>
  <p class="lead abs">Excepteur sint occaecat cupidatat proident, culpa qui officia deserunt...</p>
  <div class="dots abs"><i class="on"></i><i></i><i></i></div>
  <form class="quote abs">
    <h2>Get a Quote</h2>
    <p>Aliquip ex ea commodo consequat aute irure dolor in reprehenderit</p>
    <div class="field">Enter Name</div>
    <div class="field">Enter Email</div>
    <div class="field">Enter Address</div>
    <div class="field msg">Message</div>
    <div class="btn send">Send Message</div>
  </form>
  <svg class="curve" width="1200" height="110" viewBox="0 0 1200 110">
    <path d="M0 40 C300 100 800 95 1200 0 L1200 110 L0 110Z" fill="#0456a4"/>
    <path d="M0 60 C320 110 820 100 1200 30 L1200 110 L0 110Z" fill="#3277b5"/>
    <path d="M0 78 C330 118 830 110 1200 60 L1200 110 L0 110Z" fill="#fff"/>
  </svg>
</section>

<section class="story">
  <div class="pc abs" role="img" aria-label="Illustration of a desktop monitor showing the company name"></div>
  <h2 class="abs">Our Story...</h2>
  <div class="copy abs">
    <p>We are a team of return to work Mums available to support your office, regardless of your size. Our highly experienced team have worked for medium to large companies and are used to working with C-Level executives.</p>
    <p>We value highly motivated, intelligent, switched-on individuals who work on each project until it is finished. We thrive on delivering above expectations and love a challenge.</p>
  </div>
  <a class="btn abs">Read More</a>
</section>

<section class="team">
  <h2 class="section-title">Team Members</h2>
  <div class="member" style="left:132px"><span class="avatar" role="img" aria-label="Portrait photo of team member"></span><h3>Owen Hartley</h3><div class="role">CEO</div><p>Eiusmod tempor incididunt labore dolore magna aliqua...</p><a class="link">Click for more information</a></div>
  <div class="member" style="left:372px"><span class="avatar" role="img" aria-label="Portrait photo of team member"></span><h3>Nadia Fellows</h3><div class="role">Manager</div><p>Eiusmod tempor incididunt labore dolore magna aliqua...</p><a class="link">Click for more information</a></div>
  <div class="member" style="left:612px"><span class="avatar" role="img" aria-label="Portrait photo of team member"></span><h3>Sam Rowe</h3><div class="role">Admin</div><p>Eiusmod tempor incididunt labore dolore magna aliqua...</p><a class="link">Click for more information</a></div>
  <div class="member" style="left:852px"><span class="avatar" role="img" aria-label="Portrait photo of team member"></span><h3>Lewis Carden</h3><div class="role">Executive</div><p>Eiusmod tempor incididunt labore dolore magna aliqua...</p><a class="link">Click for more information</a></div>
</section>

<section class="services">
  <h2 class="section-title">Services</h2>
  <div class="svc" style="left:130px"><span class="ring"><svg width="50" height="50" viewBox="0 0 50 50" fill="none" stroke="#0592cd" stroke-width="2"><circle cx="25" cy="17" r="9"/><path d="M8 44c2-12 32-12 34 0z"/></svg></span><h4>Virtual Executive<br>Office Services</h4><p>Aliquip ex ea consequat. Duis aute irure dolor in reprehend...</p><a class="more" style="top:100px">Read More →</a></div>
  <div class="svc" style="left:457px"><span class="ring"><svg width="50" height="50" viewBox="0 0 50 50" fill="none" stroke="#0592cd" stroke-width="2"><rect x="12" y="8" width="26" height="34" rx="2"/><path d="M17 17h16M17 24h16M17 31h10"/></svg></span><h4>Monthly Management<br>Meetings</h4><p>Aliquip ex ea consequat. Duis aute irure dolor in reprehend...</p><a class="more" style="top:100px">Read More →</a></div>
  <div class="svc" style="left:783px"><span class="ring"><svg width="50" height="50" viewBox="0 0 50 50" fill="none" stroke="#0592cd" stroke-width="2"><path d="M8 16h12l3 4h19v22H8z"/><path d="M14 12h20v8"/></svg></span><h4>Business Advisory<br>Services</h4><p>Aliquip ex ea consequat. Duis aute irure dolor in reprehend...</p><a class="more" style="top:100px">Read More →</a></div>
  <a class="btn">View All Services</a>
</section>

<section class="blogs">
  <h2 class="section-title">Blogs</h2>
  <article class="post" style="left:130px"><div class="frame"><span class="ph" role="img" aria-label="Photo of colleagues shaking hands in a meeting"></span></div><h3>Eiusmod tempor incididunt</h3><div class="meta">20 SEP 2017 &nbsp; | &nbsp; Comments (05)</div><p>At vloreero eos et accusamus et accusamus ettodlo rsocimuupiditate non provident, simillique...</p><a class="link">Click for more information</a></article>
  <article class="post" style="left:455px"><div class="frame"><span class="ph" role="img" aria-label="Photo of a team planning with sticky notes on a table"></span></div><h3>Eiusmod tempor incididunt</h3><div class="meta">20 SEP 2017 &nbsp; | &nbsp; Comments (05)</div><p>At vloreero eos et accusamus et accusamus ettodlo rsocimuupiditate non provident, simillique...</p><a class="link">Click for more information</a></article>
  <article class="post" style="left:781px"><div class="frame"><span class="ph" role="img" aria-label="Photo of business people discussing documents"></span></div><h3>Eiusmod tempor incididunt</h3><div class="meta">20 SEP 2017 &nbsp; | &nbsp; Comments (05)</div><p>At vloreero eos et accusamus et accusamus ettodlo rsocimuupiditate non provident, simillique...</p><a class="link">Click for more information</a></article>
</section>

<section class="faqs">
  <h2 class="abs">FAQs</h2>
  <div class="faq" style="top:145px">Eiusmod tempor incididunt ut labore et dolore magna<p>Nemo enim ipsam voluptatem quia voluptas sit aspernatur aut odit aut fugit, sed quia consequuntur magni dolores eos qui ratione voluptatem...</p><a class="link">Click for more information</a></div>
  <div class="faq" style="top:263px">Eiusmod tempor incididunt ut labore et dolore magna</div>
  <div class="faq" style="top:311px">Eiusmod tempor incididunt ut labore et dolore magna</div>
  <div class="ebook abs">
    <div class="laptop abs" role="img" aria-label="Photo of a laptop with books on the screen"></div>
    <h3 class="abs">e-books</h3>
    <p class="abs">Nemo enim ipsam voluptat quia voluptas asperna...</p>
    <svg class="go abs" width="26" height="26" viewBox="0 0 26 26"><circle cx="13" cy="13" r="11" fill="none" stroke="#0592cd" stroke-width="2.5"/><path d="M8 13h9M13 9l4 4-4 4" stroke="#0592cd" stroke-width="2.5" fill="none"/></svg>
  </div>
</section>

<section class="workshops">
  <h2 class="section-title">Workshops &amp; Training</h2>
  <div class="tile" style="left:130px;top:153px" role="img" aria-label="Photo of smiling team members in an office"><span>Cashflow Planning 101</span></div>
  <div class="tile" style="left:618px;top:153px" role="img" aria-label="Photo of hands reviewing charts on a tablet"><span>Understanding the mechanics of Business</span></div>
  <div class="tile" style="left:130px;top:436px" role="img" aria-label="Photo of colleagues working at a laptop"><span>Accounting for non-accountants</span></div>
  <div class="tile" style="left:618px;top:436px" role="img" aria-label="Photo of a presenter at a whiteboard with a pie chart"><span>Tailored Training &amp; Workshops</span></div>
</section>

<section class="products">
  <h2 class="section-title">Online Products</h2>
  <div class="svc" style="left:130px;top:150px"><span class="ring"><svg width="40" height="40" viewBox="0 0 40 40" fill="none" stroke="#0592cd" stroke-width="2"><rect x="6" y="10" width="24" height="24" rx="3"/><path d="M14 26l2-6 14-14 4 4-14 14z"/></svg></span><h4>Brightwater Skills Tests<br>Accountants</h4><p>Aliquip ex ea consequat. Duis aute irure dolor in reprehend dolore magna aliqua...</p></div>
  <div class="svc" style="left:457px;top:150px"><span class="ring"><svg width="40" height="40" viewBox="0 0 40 40" fill="none" stroke="#0592cd" stroke-width="2"><rect x="5" y="8" width="30" height="20" rx="2"/><path d="M14 34h12M20 28v6"/></svg></span><h4>Brightwater Skills Tests<br>CEOs and Directors</h4><p>Aliquip ex ea consequat. Duis aute irure dolor in reprehend dolore magna aliqua...</p></div>
  <div class="svc" style="left:783px;top:150px"><span class="ring"><svg width="40" height="40" viewBox="0 0 40 40" fill="none" stroke="#0592cd" stroke-width="2"><circle cx="16" cy="22" r="6"/><path d="M16 12v4M16 28v4M6 22h4M22 22h4M9 15l3 3M20 26l3 3M9 29l3-3M20 18l3-3"/><circle cx="29" cy="11" r="4"/></svg></span><h4>Tailored Training &amp;<br>Workshops</h4><p>Aliquip ex ea consequat. Duis aute irure dolor in reprehend dolore magna aliqua...</p></div>
</section>

<section class="affiliates">
  <div class="row">
    <div class="brand"><span class="mark"></span>Brightwater Growth Horizon</div>
    <div class="brand"><span class="mark"></span>Brightwater Innovation</div>
    <div class="brand"><span class="mark"></span>Brightwater Work Set</div>
  </div>
</section>

<section class="mailing">
  <svg class="abs" style="left:195px;top:56px" width="38" height="36" viewBox="0 0 38 36" fill="none" stroke="#fff" stroke-width="2"><path d="M2 16L36 2 28 34 18 22z"/><path d="M18 22L36 2M18 22v12l5-7"/></svg>
  <h3 class="abs">JOIN MAILING LIST</h3>
  <p class="abs">Subscribe to receive updates &amp; exclusive offers.</p>
  <div class="email abs">Enter your E - mail</div>
  <div class="sub abs">SUBSCRIBE</div>
</section>

<footer class="site-footer">
  <div class="brand abs"><span class="mark"></span>Brightwater Innovation</div>
  <div class="social abs"><i></i><i></i><i></i><i></i></div>
  <div class="col abs" style="left:397px;top:52px"><h4>QUICK LINKS</h4><ul><li>Home</li><li>About us</li><li>FAQ</li><li>Case Studies</li><li>Business Advisory Services</li><li>Blos</li><li>Contact us</li></ul></div>
  <div class="col abs" style="left:590px;top:52px"><h4>NEWSLETTER</h4><p>Enter your email address to receive the latest news and notes from our blog.</p><div class="box">Enter Your Mail Id</div><div class="go">SUBSCRIBE</div></div>
  <div class="col contact abs" style="left:905px;top:52px"><h4>CONTACT INFO</h4><ul><li><i></i>(215) 555-0142</li><li><i></i>(215) 555-0142</li><li><i></i><span style="text-decoration:underline">info@brightwaterpa.example.com</span></li><li><i></i>#2868 Lorem ipsum dolor sit<br>amet, consectetur</li></ul></div>
  <div class="copyright abs">©2017 brightwaterinnovation | all rights reserved</div>
</footer>

</body>
</html>
```